Coral Ridge Networks Ltd

I need a website that is an informational only. We are a construction business building telecommunications sites. Seeing how our company is Coral Ridge the color blue might want to be incorporated in the color scheme.
I can provide more picture of towers and wireless communications if needed.
current website www.coralridgenet.ca

Industry/Entity Type

Wireless Telecommunications, Construction

Coding

Coded - Design and coding required

Number of Pages Required

2 page

Font styles to use
Sans Serif

Colors

Designer to choose colors to be used in the design.

```html
<!DOCTYPE html>
<html lang="en">
<head>
<meta charset="utf-8">
<title>Coral Ridge Ltd</title>
<link href="https://fonts.googleapis.com/css2?family=Montserrat:wght@400;500;600&display=swap" rel="stylesheet">
<style>
:root{
  --blue:#3e82c7;
  --blue-dark:#2b5c9e;
  --blue-light:#5fa9e0;
  --ink:#333a44;
  --text:#4a4f57;
  --white:#ffffff;
  --footer-text:#ffffff;
  --btn-dark:#3a404a;
}
*{box-sizing:border-box;margin:0;padding:0}
html,body{width:1200px;height:2265px;overflow:hidden}
body{font-family:'Montserrat',sans-serif;color:var(--text);background:var(--white);position:relative}
.btn{display:inline-flex;align-items:center;justify-content:center;border-radius:20px;color:var(--white);
  background:linear-gradient(90deg,var(--blue-light),var(--blue-dark));text-decoration:none;
  box-shadow:0 4px 8px rgba(40,80,140,.35);font-weight:500}
.hero{position:absolute;left:0;top:0;width:1200px;height:1100px;
  background:linear-gradient(180deg,#5d6a66 0%,#4c5a44 25%,#5b5543 50%,#6b6459 62%,#8f8f8f 80%,#ffffff 100%)}
.header{position:absolute;left:135px;top:0;width:926px;height:76px;background:rgba(255,255,255,.93);display:flex;align-items:center;padding:0 17px}
.brand{font-size:30px;font-weight:500;color:var(--blue);letter-spacing:-.5px}
.nav{margin-left:auto;display:flex;align-items:center;gap:29px;font-size:16px;color:var(--ink)}
.nav a{color:var(--ink);text-decoration:none}
.nav a.active{color:var(--blue)}
.nav .btn{width:153px;height:26px;font-size:14px;margin-left:2px;font-weight:400}
.hero-copy{position:absolute;left:0;top:300px;width:1200px;text-align:center;color:var(--white)}
.hero-copy h1{font-size:52px;font-weight:500;line-height:1.1}
.hero-copy p{width:490px;margin:8px auto 0;text-align:left;font-size:16px;line-height:21px}
.hero-copy .btn{width:151px;height:35px;font-size:14px;margin-top:16px;font-weight:400}
.dots{display:flex;justify-content:center;gap:6px;margin-top:14px}
.dots span{width:13px;height:13px;border:2px solid var(--white);border-radius:50%}
.dots span.on{background:var(--blue);width:16px;height:16px;margin-top:-1.5px}
.about{position:absolute;left:135px;top:628px;width:926px;height:420px;text-align:center;
  background:linear-gradient(180deg,#fff 0%,#fff 80%,rgba(255,255,255,0) 100%)}
.eyebrow{font-size:17px;color:var(--ink);text-transform:uppercase}
.about .eyebrow{margin-top:60px}
.title{font-size:54px;font-weight:600;line-height:1.2;color:var(--blue)}
.about .title{background:linear-gradient(90deg,var(--blue-light),var(--blue-dark));-webkit-background-clip:text;background-clip:text;color:transparent;display:inline-block}
.about p{width:680px;margin:18px auto 0;font-size:16px;line-height:23px}
.about p:first-of-type{margin-top:12px}
.about .call{color:var(--blue-dark)}
.about-btn{position:absolute;left:523px;top:1033px;width:151px;height:37px;font-size:14px}
.services{position:absolute;left:0;top:1200px;width:1200px;text-align:center}
.services .eyebrow{font-size:14px;margin-top:17px}
.services .title{color:var(--ink);margin-top:-2px}
.services .title em{font-style:normal;color:var(--blue)}
.footer-bg{position:absolute;left:0;top:1650px;width:1200px;height:615px;
  background:linear-gradient(180deg,rgba(255,255,255,0) 0%,#dfe6f0 18%,#a6b6d0 42%,#8da2c6 70%,#9eb0cf 100%)}
.cards{position:absolute;left:156px;top:1326px;display:flex;gap:13px}
.card{width:286px;height:376px;background:var(--white);text-align:center;box-shadow:0 2px 8px rgba(0,0,0,.08)}
.card .photo{height:186px}
.card h3{font-size:18px;font-weight:500;color:var(--ink);margin-top:27px}
.card.featured h3{color:var(--blue)}
.card p{font-size:12.5px;line-height:19px;margin:9px 8px 0;height:57px;overflow:hidden}
.card .btn{width:103px;height:27px;font-size:11.5px;margin-top:12px;background:var(--btn-dark);box-shadow:none;gap:12px}
.card.featured .btn{background:linear-gradient(90deg,var(--blue-light),var(--blue))}
.footer{position:absolute;left:0;top:1900px;width:1200px;height:365px;color:var(--footer-text)}
.footer h4{font-size:16px;font-weight:600;text-transform:uppercase}
.news{position:absolute;left:136px;top:6px;width:300px}
.news p{font-size:14px;line-height:22px;margin-top:32px}
.news .field{width:293px;height:42px;border-radius:21px;background:var(--white);margin-top:16px;font-size:13px;color:#555;padding:13px 17px}
.news .btn{width:148px;height:38px;font-size:16px;margin-top:15px;border-radius:19px}
.contact{position:absolute;left:528px;top:6px;width:300px}
.contact ul{list-style:none;margin-top:26px}
.contact li{display:flex;gap:18px;font-size:16px;line-height:22px;margin-bottom:14px}
.contact svg{flex:none;margin-top:2px}
.footer-brand{position:absolute;left:896px;top:6px;width:164px;height:123px;background:var(--white);display:flex;align-items:center;justify-content:center;font-size:28px;font-weight:500;color:var(--blue)}
.social{position:absolute;left:896px;top:180px;display:flex;gap:12px}
.social span{width:33px;height:33px;border:1.5px solid var(--white);border-radius:50%}
.copyright{position:absolute;left:0;top:2187px;width:1200px;text-align:center;font-size:12.5px;color:var(--white)}
</style>
</head>
<body>
<div class="hero" role="img" aria-label="Photo of a mountain construction site with concrete tower footings, an excavator and forest"></div>

<header class="header">
  <div class="brand">coral ridge</div>
  <nav class="nav">
    <a class="active" href="#">home</a>
    <a href="#">about us</a>
    <a href="#">services</a>
    <a href="#">contact us</a>
    <a class="btn" href="#">get a free quote</a>
  </nav>
</header>

<section class="hero-copy">
  <h1>Coral Ridge Ltd</h1>
  <p>Our courteous, professional team is able to support a range of services to meet your requirements</p>
  <a class="btn" href="#">get a free quote</a>
  <div class="dots"><span></span><span class="on"></span><span></span><span></span></div>
</section>

<section class="about">
  <div class="eyebrow">About us</div>
  <h2 class="title">coral ridge</h2>
  <p>At Coral Ridge Ltd, we are dedicated to providing our customers with friendly professional service. We value your business. We have made it our mission to provide reliable products and services in our customer-driven approach.</p>
  <p>Our courteous, professional team is able to support a range of services to meet your requirements.</p>
  <p>To learn more about Coral Ridge Ltd, and the products and services we can offer, <span class="call">please call us at 1-604-555-0143.</span></p>
</section>
<a class="btn about-btn" href="#">Read More Us</a>

<div class="footer-bg" role="img" aria-label="Photo of a snow-covered mountain summit"></div>

<section class="services">
  <div class="eyebrow">Coral Ridge Communications</div>
  <h2 class="title">our <em>services</em></h2>
</section>

<div class="cards">
  <article class="card">
    <div class="photo" role="img" aria-label="Photo of rooftop telecom equipment cabinets and antennas" style="background:linear-gradient(180deg,#3d6fb3 0%,#9fb4cc 40%,#d9dde0 70%,#8d9094 100%)"></div>
    <h3>Rooftop Sites</h3>
    <p>Structural upgrades or simple ballast mounts. Shelter on the ground, leasehold build outs or cabinets on the roof.</p>
    <a class="btn" href="#">Read More <svg width="11" height="10" viewBox="0 0 11 10"><path d="M0 5h9M5.5 1 9.5 5 5.5 9" stroke="#fff" stroke-width="2" fill="none"/></svg></a>
  </article>
  <article class="card featured">
    <div class="photo" role="img" aria-label="Photo of a lattice tower with a microwave dish" style="background:linear-gradient(180deg,#3f5f8a 0%,#5a7598 50%,#8797ab 75%,#4b6386 100%)"></div>
    <h3>Towers and Monopoles</h3>
    <p>Coral Ridge can engineer, supply and install all your tower needs. New structures or existing, call us for pricing we would be</p>
    <a class="btn" href="#">Read More <svg width="11" height="10" viewBox="0 0 11 10"><path d="M0 5h9M5.5 1 9.5 5 5.5 9" stroke="#fff" stroke-width="2" fill="none"/></svg></a>
  </article>
  <article class="card">
    <div class="photo" role="img" aria-label="Photo of solar panels on a green monopole above trees" style="background:linear-gradient(90deg,#0f6b55 0%,#1c8a6c 30%,#6d7f5a 60%,#8a7a4c 100%)"></div>
    <h3>In Building</h3>
    <p>Small office or large Hotel. Coral Ridge has installed services into all size buildings. Fiber, cat6, or coax, we have the abilities to</p>
    <a class="btn" href="#">Read More <svg width="11" height="10" viewBox="0 0 11 10"><path d="M0 5h9M5.5 1 9.5 5 5.5 9" stroke="#fff" stroke-width="2" fill="none"/></svg></a>
  </article>
</div>

<footer class="footer">
  <div class="news">
    <h4>Sign up for newsletter</h4>
    <p>excepteur sint occaecat cupidatat-proident, sunt in culpa</p>
    <div class="field">Enter email</div>
    <a class="btn" href="#">SUBSCRIBE</a>
  </div>
  <div class="contact">
    <h4>Contact us</h4>
    <ul>
      <li><svg width="16" height="20" viewBox="0 0 16 20"><path d="M8 0a8 8 0 0 0-8 8c0 6 8 12 8 12s8-6 8-12a8 8 0 0 0-8-8zm0 11a3 3 0 1 1 0-6 3 3 0 0 1 0 6z" fill="#fff"/></svg><span>Address.<br>4417 Harbourview Rd, Langley, BC<br>V2Y 0Z0</span></li>
      <li><svg width="18" height="18" viewBox="0 0 18 18"><path d="M4 0l3 4-2 3c1 2 4 5 6 6l3-2 4 3-2 4C8 18 0 10 0 2z" fill="#fff"/></svg><span>Phone:<br>1-604-555-0143</span></li>
      <li><svg width="18" height="14" viewBox="0 0 18 14"><rect width="18" height="14" rx="1" fill="#fff"/><path d="M1 1l8 7 8-7" stroke="#8da2c6" stroke-width="1.6" fill="none"/></svg><span>Email:<br>info@coralridgenet.ca</span></li>
    </ul>
  </div>
  <div class="footer-brand">coral ridge</div>
  <div class="social" aria-label="Social media links"><span></span><span></span><span></span><span></span></div>
</footer>

<div class="copyright">Copyright © 2022 Coral Ridge Ltd. All rights reserved. Privacy Policy. Terms &amp; Conditions.</div>
</body>
</html>
```